Pinecrest Realty Property Management Team

We’re going to send out post cards to our neighborhood to potential Investment Property Owners to inform them about our Property Management Services. Looking for something clear, simple, easy to read, not too busy, gets straight to the point. Here’s some verbiage we’d be looking to include, open to different arrangements and ideas.
FREE Property Management for your first 2 months! OR
Your first 2 months of Property Management are FREE!
Get peace of mind with the Pinecrest Realty way! We lease your property faster and for maximum rent!
Professional Services at the Highest Standard:
• Securing Qualified Tenants
• Collection of Rents
• Managing Maintenance & Repairs
• Staying Current with Rental Laws
• Tenant Management
• Distributing Financial Reports
• Manage & Pay Bills
• Income Property Purchases & Sales
With over 30 years of combined experience we help our Owners reduce liability by using all the proper lease and disclosure contracts and staying current with Rental Laws.
We use advanced technology systems to help:
• Respond faster & provide better services to both owners and tenants.
• Address property maintenance issues faster.
• Process payments faster & more securely.
• Allow our tenants to pay rent online.
• Market your properties & fill vacancies sooner.
• Email statements directly to you as well as have them available at any time.
Our Executive Property Management Team:
Bartholomew K. Fenwick, Broker/Sr. Property Manager
Raul Ortiz, Sr. Property Manager, “Yo Halbo Espanol”
Marla Quist, Office Manager
Pinecrest Realty, Inc.
482 W. 6th Ave., Suite 207
Seacliff Bay, CA 93421
Office: (555) 274-9182
Cell (555) 639-5027
www.PinecrestRealty.example
DRE #07416352
Note: feel free to get rid of the background of our Team Photo if that works better, hopefully it's set up to easily clear that out if needed. I attached full and reduced versions in case one or the other is preferred.
Target Market(s)
Investors, property owners, San Luis Obispo County, CA, USA
Industry/Entity Type
Property Management
Colors
Designer to choose colors to be used in the design.
Look and feel

```html
<!DOCTYPE html>
<html lang="en">
<head>
<meta charset="utf-8">
<title>Pinecrest Realty Postcard</title>
<link href="https://fonts.googleapis.com/css2?family=Montserrat:wght@600;700;800&family=Nunito+Sans:wght@400;600;700&display=swap" rel="stylesheet">
<style>
:root{
  --purple:#5b3471;
  --green:#2f9e41;
  --green-dark:#1f8a32;
  --green-light:#8fdf8f;
  --green-mid:#54c167;
  --ink:#2e2e2e;
  --page:#ececec;
  --white:#ffffff;
  --rule:#d6d6d6;
}
*{box-sizing:border-box;margin:0;padding:0}
html,body{width:896px;height:1200px;overflow:hidden}
body{background:var(--page);font-family:"Nunito Sans",sans-serif;color:var(--ink);position:relative}
.card{position:absolute;left:51px;width:789px;height:511px;background:var(--white);overflow:hidden;box-shadow:0 6px 14px rgba(0,0,0,.18)}
.card--front{top:47px}
.card--back{top:619px}
.abs{position:absolute}
.brand{font-family:"Montserrat",sans-serif;font-weight:800;color:var(--green);line-height:1.05;display:flex;align-items:center;gap:8px}
.brand__mark{width:14px;height:14px;background:var(--green);flex:none}
.brand--front{left:22px;top:30px;font-size:24px;width:160px}
.headline{left:22px;top:122px;font-family:"Montserrat",sans-serif;font-size:32px;line-height:40px;color:var(--green);font-weight:600}
.headline strong{color:var(--purple);font-weight:800}
.tagline{left:0;top:245px;width:470px;height:48px;background:var(--purple);clip-path:polygon(0 0,440px 0,100% 100%,0 100%);color:var(--white);padding:6px 0 0 20px}
.tagline b{display:block;font-family:"Montserrat",sans-serif;font-weight:800;font-size:14px;letter-spacing:-.3px}
.tagline span{display:block;font-size:14px;line-height:18px}
.pill{font-family:"Montserrat",sans-serif;font-weight:800;color:var(--white);border-radius:14px;text-align:center}
.pill--services{left:106px;top:301px;width:282px;height:30px;background:var(--green);font-size:18px;line-height:30px;border:2px solid var(--green-dark)}
.list{list-style:none;font-size:13.5px;line-height:17px}
.list li{position:relative;padding-left:19px;margin-bottom:7px}
.list li::before{content:"";position:absolute;left:0;top:4px;width:10px;height:10px;border-radius:50%;background:var(--purple);
  background-image:linear-gradient(45deg,transparent 45%,#fff 45%,#fff 55%,transparent 55%);}
.list--a{left:21px;top:343px;width:250px}
.list--b{left:274px;top:342px;width:260px}
.contactbar{left:0;top:465px;width:100%;height:38px;background:var(--purple);color:var(--white);display:flex;justify-content:center;align-items:center;gap:22px;font-size:17px}
.contactbar span{display:flex;align-items:center;gap:8px}
.greenstrip{left:0;bottom:0;width:100%;height:8px;background:var(--green)}
.ico{width:17px;height:17px;flex:none}
.intro{left:0;top:0;width:450px;height:78px;background:var(--green);clip-path:polygon(0 0,425px 0,100% 100%,0 100%);color:var(--white);font-family:"Montserrat",sans-serif;font-weight:700;font-size:12.6px;line-height:18.5px;padding:11px 30px 0 17px}
.pill--tech{left:42px;top:91px;width:377px;height:31px;background:var(--purple);font-size:18.5px;line-height:31px}
.checks{left:26px;top:133px;width:440px;list-style:none;font-size:12.8px;line-height:13px}
.checks li{position:relative;padding-left:15px;margin-bottom:8px}
.checks li::before{content:"";position:absolute;left:0;top:1px;width:10px;height:10px;border-radius:50%;background:var(--green)}
.team{top:291px;width:130px;text-align:center}
.team__photo{width:74px;height:74px;border-radius:50%;margin:0 auto 14px;background:radial-gradient(circle at 50% 40%,#e2e2e2,#c9c9c9);border:4px solid #f2f2f2;box-shadow:0 2px 4px rgba(0,0,0,.12)}
.team__name{font-family:"Montserrat",sans-serif;font-weight:700;color:var(--purple);font-size:12.5px;white-space:nowrap}
.team__role{font-size:10.5px;line-height:13px}
.office{left:0;top:430px;width:341px;height:70px;background:var(--purple);border-radius:0 8px 8px 0;color:var(--white);padding:4px 0 0 13px;font-size:11.8px;line-height:15.5px}
.office b{font-family:"Montserrat",sans-serif;font-weight:700;font-size:12px;text-transform:uppercase;padding-left:17px}
.office div{display:flex;align-items:center;gap:5px}
.ico--s{width:11px;height:11px;flex:none}
.greenstrip--back{left:0;top:498px;width:341px;height:13px;border-radius:0 6px 0 0}
.brand--back{left:496px;top:30px;font-size:20px;width:110px}
.return{left:486px;top:98px;width:130px;text-align:center;font-size:9.5px;line-height:14px}
.stamp{left:670px;top:21px;width:94px;height:114px;border:1px solid var(--rule)}
.addrline{left:525px;width:239px;height:1px;background:var(--rule)}
</style>
</head>
<body>

<section class="card card--front">
  <svg class="abs" style="left:400px;top:0" width="389" height="420" viewBox="400 0 389 420" aria-hidden="true">
    <circle cx="640" cy="160" r="240" fill="var(--green-dark)"/>
    <circle cx="660" cy="150" r="226" fill="var(--green-light)"/>
    <circle cx="672" cy="145" r="218" fill="var(--green-mid)"/>
    <circle cx="665" cy="130" r="208" fill="var(--white)"/>
  </svg>
  <svg class="abs" style="left:450px;top:0" width="339" height="340" viewBox="450 0 339 340" role="img" aria-label="Photo of the three-person property management team smiling against a warm light wall">
    <defs>
      <linearGradient id="teamPhoto" x1="0" y1="0" x2="0" y2="1">
        <stop offset="0" stop-color="#efe4d6"/>
        <stop offset="1" stop-color="#6b88b8"/>
      </linearGradient>
    </defs>
    <circle cx="665" cy="130" r="200" fill="url(#teamPhoto)"/>
  </svg>

  <div class="abs brand brand--front"><span class="brand__mark"></span>Pinecrest Realty</div>

  <h1 class="abs headline"><strong>FREE</strong> Property<br>Management For Your<br><strong>First 2 Months!</strong></h1>

  <div class="abs tagline">
    <b>GET PEACE OF MIND WITH THE PINECREST REALTY WAY!</b>
    <span>We lease your property faster and for maximum rent!</span>
  </div>

  <div class="abs pill pill--services">PROFESSIONAL SERVICES</div>

  <ul class="abs list list--a">
    <li>Securing Qualified Tenants</li>
    <li>Collection of Rents</li>
    <li>Managing Maintenance<br>&amp; Repairs</li>
    <li>Staying Current with Rental Laws</li>
  </ul>
  <ul class="abs list list--b">
    <li>Tenant Management</li>
    <li>Distributing Financial Reports</li>
    <li>Manage &amp; Pay Bills</li>
    <li>Income Property Purchases<br>&amp; Sales</li>
  </ul>

  <div class="abs contactbar">
    <span><svg class="ico" viewBox="0 0 20 20"><circle cx="10" cy="10" r="10" fill="#fff"/><rect x="5" y="8" width="10" height="6" rx="1" fill="var(--purple)"/><path d="M5 7q5-3 10 0" stroke="var(--purple)" stroke-width="2" fill="none"/></svg>(555) 274-9182</span>
    <span><svg class="ico" viewBox="0 0 20 20"><circle cx="10" cy="10" r="10" fill="#fff"/><path d="M7 5l2 3-1 1q1 2 3 3l1-1 3 2-1 2q-5 0-8-6z" fill="var(--purple)"/></svg>(555) 639-5027</span>
    <span><svg class="ico" viewBox="0 0 20 20"><circle cx="10" cy="10" r="10" fill="#fff"/><circle cx="10" cy="10" r="5.5" fill="none" stroke="var(--purple)" stroke-width="1.3"/><path d="M4.5 10h11M10 4.5q-3 5.5 0 11q3-5.5 0-11" fill="none" stroke="var(--purple)" stroke-width="1.2"/></svg>www.PinecrestRealty.example</span>
  </div>
  <div class="abs greenstrip"></div>
</section>

<section class="card card--back">
  <p class="abs intro">With over 30 years of combined experience we help our Owners reduce liability by using all the proper lease and disclosure contracts and staying current with Rental Laws.</p>

  <div class="abs pill pill--tech">ADVANCED TECHNOLOGY SYSTEMS</div>

  <ul class="abs checks">
    <li>Respond faster &amp; provide better services to both owners and tenants.</li>
    <li>Address property maintenance issues faster.</li>
    <li>Process payments faster &amp; more securely.</li>
    <li>Allow our tenants to pay rent online.</li>
    <li>Market your properties &amp; fill vacancies sooner.</li>
    <li>Email statements directly to you as well as have them available at any time.</li>
  </ul>

  <div class="abs team" style="left:26px">
    <div class="team__photo" role="img" aria-label="Portrait placeholder for Bartholomew K. Fenwick"></div>
    <div class="team__name">Bartholomew K. Fenwick</div>
    <div class="team__role">Broker/Sr.<br>Property Manager</div>
  </div>
  <div class="abs team" style="left:182px">
    <div class="team__photo" role="img" aria-label="Portrait placeholder for Raul Ortiz"></div>
    <div class="team__name">Raul Ortiz</div>
    <div class="team__role">Sr. Property Manager,<br>“Yo Halbo Espanol”</div>
  </div>
  <div class="abs team" style="left:322px">
    <div class="team__photo" role="img" aria-label="Portrait placeholder for Marla Quist"></div>
    <div class="team__name">Marla Quist</div>
    <div class="team__role">Office Manager</div>
  </div>

  <div class="abs office">
    <b>Pinecrest Realty, Inc.</b>
    <div><svg class="ico--s" viewBox="0 0 12 12"><path d="M6 0a4 4 0 014 4c0 3-4 8-4 8S2 7 2 4a4 4 0 014-4z" fill="#fff"/><circle cx="6" cy="4" r="1.5" fill="var(--purple)"/></svg>482 W. 6th Ave., Suite 207 Seacliff Bay, CA 93421</div>
    <div><svg class="ico--s" viewBox="0 0 12 12"><circle cx="6" cy="6" r="6" fill="#fff"/><rect x="3" y="5" width="6" height="4" fill="var(--purple)"/></svg>(555) 274-9182 &nbsp;&nbsp;<svg class="ico--s" viewBox="0 0 12 12"><circle cx="6" cy="6" r="6" fill="#fff"/><path d="M4 3l1 2-.6.6q.6 1.2 1.8 1.8l.6-.6 2 1-.6 1.2q-3 0-4.6-3.8z" fill="var(--purple)"/></svg>(555) 639-5027</div>
    <div><svg class="ico--s" viewBox="0 0 12 12"><circle cx="6" cy="6" r="6" fill="#fff"/><circle cx="6" cy="6" r="3" fill="none" stroke="var(--purple)"/></svg>www.PinecrestRealty.example</div>
  </div>
  <div class="abs greenstrip greenstrip--back"></div>

  <div class="abs brand brand--back"><span class="brand__mark"></span>Pinecrest Realty</div>
  <p class="abs return">482 W. 6th Ave., Suite 207<br>Seacliff Bay, CA 93421</p>

  <div class="abs stamp"></div>
  <div class="abs addrline" style="top:233px"></div>
  <div class="abs addrline" style="top:273px"></div>
  <div class="abs addrline" style="top:309px"></div>
  <div class="abs addrline" style="top:347px"></div>
</section>

</body>
</html>
```